Health & Wellness Contest - The Bright Harvest Renewal

We need a postcard design that is professional and grabs the attention of people who see it. The postcard will be left in fitness centers and posted on social media. The front of the card MUST look amazing - make potential participants want to pick it up and find out more information; the back of the card will have the contest details. The goal is to have people sign up for a 90 day fitness program, and most of the marketing will be with this postcard.

Target Market(s)

People that are thinking about beginning a health regiment; people who are already used to exercising and are willing to try a new supplement

Industry/Entity Type

Health And Wellness

Colors

Designer to choose colors to be used in the design.

Requirements
Must have
• Front Cover -- Must have the phrase "The Bright Harvest Renewal" and must have "$2,500 Grand Prize"; and must have "BrightHarvestRenewal.com"
Nice to have
• Design on Front; Details on Back; appeal to both men and women

```html
<!DOCTYPE html>
<html lang="en">
<head>
<meta charset="utf-8">
<title>The Bright Harvest Renewal – Postcard</title>
<link href="https://fonts.googleapis.com/css2?family=Marcellus&family=Lato:wght@400;700&family=Alegreya:wght@400;700&family=Merriweather:wght@400&display=swap" rel="stylesheet">
<style>
  :root {
    --blue: #1a5aa6;
    --green: #8cc63f;
    --green-dark: #3d9a2f;
    --gold: #f3b71b;
    --gold-edge: #fbd45a;
    --white: #ffffff;
    --page: #ecebe8;
    --photo-light: #e9e2da;
    --photo-warm: #c99677;
  }
  * { box-sizing: border-box; margin: 0; padding: 0; }
  html, body { width: 948px; height: 1200px; overflow: hidden; }
  body { background: var(--page); position: relative; font-family: "Lato", sans-serif; }

  .postcard {
    position: absolute; left: 124px; width: 632px; height: 488px;
    background: var(--white); overflow: hidden;
    box-shadow: 0 3px 10px rgba(0,0,0,.25);
  }
  .postcard--front { top: 82px; }
  .postcard--back { top: 626px; }

  .postcard__shapes { position: absolute; inset: 0; }

  .title { position: absolute; left: 10px; width: 300px; text-align: center; font-family: "Marcellus", serif; color: var(--green); }
  .title__lead { font-size: 28px; line-height: 1; }
  .title__main { font-size: 40px; line-height: 1.1; letter-spacing: 1px; margin-top: 6px; }
  .title__rule { position: relative; width: 226px; height: 2px; background: var(--green); margin: 8px auto 0; }
  .title__rule::after { content: ""; position: absolute; left: 50%; top: -2px; width: 5px; height: 5px; margin-left: -2.5px; border-radius: 50%; background: var(--green); }

  .mission { position: absolute; left: 10px; width: 300px; text-align: center; color: var(--white); font-size: 11px; font-weight: 700; line-height: 1.35; }

  .invite-band { position: absolute; left: 0; top: 196px; width: 292px; height: 60px; background: var(--white); display: flex; align-items: center; justify-content: center; text-align: center; color: var(--green-dark); font-size: 11.5px; font-weight: 700; line-height: 1.3; }

  .benefits { position: absolute; left: 18px; top: 278px; width: 270px; display: grid; grid-template-columns: 136px 134px; row-gap: 6px; list-style: none; font-family: "Alegreya", serif; font-size: 11px; color: var(--white); }
  .benefits li { display: flex; align-items: center; gap: 6px; white-space: nowrap; }
  .benefits svg { flex: none; }

  .deadline { position: absolute; background: var(--green); color: var(--white); border: 2px solid var(--white); border-radius: 26px; display: flex; align-items: center; }
  .postcard--front .deadline { left: 14px; top: 393px; width: 386px; height: 48px; font-size: 13.5px; padding-left: 22px; }
  .postcard--back .deadline { left: 20px; top: 200px; width: 256px; height: 51px; font-size: 13px; line-height: 1.25; padding-left: 24px; }

  .prize-badge { position: absolute; width: 110px; height: 110px; z-index: 2; }
  .prize-badge__text { position: absolute; inset: 0; display: flex; flex-direction: column; align-items: center; justify-content: center; color: var(--white); }
  .prize-badge__label { font-size: 11px; }
  .prize-badge__amount { font-family: "Lato", sans-serif; font-weight: 700; font-size: 18px; margin-top: 2px; }
  .postcard--front .prize-badge { left: 382px; top: 356px; }
  .postcard--back .prize-badge { left: 292px; top: 180px; }

  .site-link { position: absolute; color: var(--white); font-size: 11px; font-weight: 700; left: 0; width: 300px; top: 456px; text-align: center; }

  .photo { position: absolute; }
  .photo--couple { left: 300px; top: 0; width: 332px; height: 488px; background: linear-gradient(160deg, var(--photo-light) 0%, var(--photo-warm) 55%, #e7a24a 100%); }
  .photo--torsos { left: 96px; top: 254px; width: 250px; height: 146px; background: linear-gradient(90deg, #c89a80 0%, #8a7b78 50%, #d2a98e 100%); z-index: 1; }

  .sign-up { position: absolute; left: 30px; top: 342px; font-family: "Merriweather", serif; font-size: 34px; color: var(--white); letter-spacing: .5px; z-index: 1; }
  .web-band { position: absolute; left: 0; top: 400px; width: 350px; height: 34px; background: var(--white); display: flex; align-items: center; justify-content: center; color: var(--green); font-weight: 700; font-size: 15px; }
  .sponsor-note { position: absolute; left: 0; top: 440px; width: 350px; text-align: center; color: var(--white); font-size: 11px; line-height: 1.3; }

  .stamp-box { position: absolute; left: 513px; top: 30px; width: 99px; height: 73px; border: 1.5px solid #b9b9b9; }
</style>
</head>
<body>

<section class="postcard postcard--front" aria-label="Postcard front">
  <div class="photo photo--couple" role="img" aria-label="Photo of a smiling fit woman and man holding a bathroom scale and a measuring tape"></div>
  <svg class="postcard__shapes" width="632" height="488" viewBox="0 0 632 488">
    <path d="M0 0 H352 Q290 180 296 488 H0 Z" fill="var(--blue)"/>
    <path d="M352 0 Q290 180 296 488" fill="none" stroke="var(--white)" stroke-width="12"/>
    <path d="M362 0 Q298 180 304 488" fill="none" stroke="var(--green)" stroke-width="10"/>
  </svg>

  <div class="title" style="top:30px">
    <div class="title__lead">The Bright Harvest</div>
    <div class="title__main">RENEWAL</div>
    <div class="title__rule"></div>
  </div>
  <p class="mission" style="top:152px">The Bright Harvest Renewal has one mission<br>to help people be a better version of themselves.</p>

  <div class="invite-band">Join us in the Bright Harvest Renewal<br>and experience some of the benefits that<br>countless others have seen:</div>

  <ul class="benefits">
    <li><svg width="9" height="9" viewBox="0 0 10 10"><circle cx="5" cy="5" r="4.2" fill="none" stroke="var(--green)" stroke-width="1.2"/><path d="M3 5.2 L4.5 6.6 L7.2 3.6" fill="none" stroke="var(--green)" stroke-width="1.2"/></svg>Better health</li>
    <li><svg width="9" height="9" viewBox="0 0 10 10"><circle cx="5" cy="5" r="4.2" fill="none" stroke="var(--green)" stroke-width="1.2"/><path d="M3 5.2 L4.5 6.6 L7.2 3.6" fill="none" stroke="var(--green)" stroke-width="1.2"/></svg>Increased awareness</li>
    <li><svg width="9" height="9" viewBox="0 0 10 10"><circle cx="5" cy="5" r="4.2" fill="none" stroke="var(--green)" stroke-width="1.2"/><path d="M3 5.2 L4.5 6.6 L7.2 3.6" fill="none" stroke="var(--green)" stroke-width="1.2"/></svg>Appetite suppression</li>
    <li><svg width="9" height="9" viewBox="0 0 10 10"><circle cx="5" cy="5" r="4.2" fill="none" stroke="var(--green)" stroke-width="1.2"/><path d="M3 5.2 L4.5 6.6 L7.2 3.6" fill="none" stroke="var(--green)" stroke-width="1.2"/></svg>Better mood</li>
    <li><svg width="9" height="9" viewBox="0 0 10 10"><circle cx="5" cy="5" r="4.2" fill="none" stroke="var(--green)" stroke-width="1.2"/><path d="M3 5.2 L4.5 6.6 L7.2 3.6" fill="none" stroke="var(--green)" stroke-width="1.2"/></svg>Better energy</li>
    <li><svg width="9" height="9" viewBox="0 0 10 10"><circle cx="5" cy="5" r="4.2" fill="none" stroke="var(--green)" stroke-width="1.2"/><path d="M3 5.2 L4.5 6.6 L7.2 3.6" fill="none" stroke="var(--green)" stroke-width="1.2"/></svg>Muscle preservation</li>
    <li><svg width="9" height="9" viewBox="0 0 10 10"><circle cx="5" cy="5" r="4.2" fill="none" stroke="var(--green)" stroke-width="1.2"/><path d="M3 5.2 L4.5 6.6 L7.2 3.6" fill="none" stroke="var(--green)" stroke-width="1.2"/></svg>Fat Loss</li>
    <li><svg width="9" height="9" viewBox="0 0 10 10"><circle cx="5" cy="5" r="4.2" fill="none" stroke="var(--green)" stroke-width="1.2"/><path d="M3 5.2 L4.5 6.6 L7.2 3.6" fill="none" stroke="var(--green)" stroke-width="1.2"/></svg>Better sleep</li>
    <li><svg width="9" height="9" viewBox="0 0 10 10"><circle cx="5" cy="5" r="4.2" fill="none" stroke="var(--green)" stroke-width="1.2"/><path d="M3 5.2 L4.5 6.6 L7.2 3.6" fill="none" stroke="var(--green)" stroke-width="1.2"/></svg>Better focus</li>
    <li><svg width="9" height="9" viewBox="0 0 10 10"><circle cx="5" cy="5" r="4.2" fill="none" stroke="var(--green)" stroke-width="1.2"/><path d="M3 5.2 L4.5 6.6 L7.2 3.6" fill="none" stroke="var(--green)" stroke-width="1.2"/></svg>And much more...</li>
  </ul>

  <div class="deadline">Challenge Deadline: Register by October 31, 2017.</div>

  <div class="prize-badge">
    <svg width="110" height="110" viewBox="0 0 110 110">
      <circle cx="55" cy="55" r="53" fill="var(--gold-edge)"/>
      <circle cx="55" cy="55" r="50" fill="var(--white)"/>
      <circle cx="55" cy="55" r="46" fill="var(--gold)"/>
      <circle cx="55" cy="55" r="40" fill="none" stroke="var(--white)" stroke-width="1" stroke-dasharray="2 2"/>
    </svg>
    <div class="prize-badge__text"><span class="prize-badge__label">Grand Prize</span><span class="prize-badge__amount">$2,500.00</span></div>
  </div>

  <div class="site-link">www.BrightHarvestRenewal.com</div>
</section>

<section class="postcard postcard--back" aria-label="Postcard back">
  <svg class="postcard__shapes" width="632" height="488" viewBox="0 0 632 488">
    <path d="M0 0 H288 Q372 200 350 488 H0 Z" fill="var(--blue)"/>
    <path d="M288 0 Q372 200 350 488" fill="none" stroke="var(--white)" stroke-width="10"/>
    <path d="M298 0 Q382 200 360 488" fill="none" stroke="var(--green)" stroke-width="9"/>
  </svg>

  <div class="title" style="top:24px">
    <div class="title__lead">The Bright Harvest</div>
    <div class="title__main">RENEWAL</div>
    <div class="title__rule"></div>
  </div>
  <p class="mission" style="top:148px">The Bright Harvest Renewal has one mission<br>to help people be a better version of themselves.</p>

  <div class="photo photo--torsos" role="img" aria-label="Photo of a man's and a woman's toned torsos"></div>
  <div class="sign-up">sign up</div>

  <div class="deadline">Challenge Deadline:<br>Register by October 31, 2017.</div>

  <div class="prize-badge">
    <svg width="110" height="110" viewBox="0 0 110 110">
      <circle cx="55" cy="55" r="53" fill="var(--gold-edge)"/>
      <circle cx="55" cy="55" r="50" fill="var(--white)"/>
      <circle cx="55" cy="55" r="46" fill="var(--gold)"/>
      <circle cx="55" cy="55" r="40" fill="none" stroke="var(--white)" stroke-width="1" stroke-dasharray="2 2"/>
    </svg>
    <div class="prize-badge__text"><span class="prize-badge__label">Grand Prize</span><span class="prize-badge__amount">$2,500.00</span></div>
  </div>

  <div class="web-band">www.BrightHarvestRenewal.com</div>
  <p class="sponsor-note">For Challenge details, email one of our sponsors at<br>Info@NorthgateCounsel.Org</p>

  <div class="stamp-box" aria-label="Stamp area"></div>
</section>

</body>
</html>
```